ashby paving works

Needs to have phone number 0412885107 and email marklowry@pavemail.com.au.
ABN 27613048852
name mark lowry

For all your concreting solutions
Excavation
Exposed & colour concrete
House & shed slabs
Driveways
Landing & steps

Contact Information for Business Card

ph 0412885107
email marklowry@pavemail.com.au.
ABN 27613048852
name mark lowry

```html
<!DOCTYPE html>
<html lang="en">
<head>
<meta charset="utf-8">
<title>Ashby Paving Works – Business Cards</title>
<link rel="stylesheet" href="https://fonts.googleapis.com/css2?family=Lato:wght@300;400;700;900&family=Montserrat:wght@300;400;600;700&display=swap">
<style>
  :root {
    --orange: #f26b22;
    --grey: #636363;
    --ink: #2b2b2b;
    --paper: #ffffff;
    --backdrop: #3a3d42;
  }
  * { margin: 0; padding: 0; box-sizing: border-box; }
  html, body { width: 1200px; height: 1200px; overflow: hidden; }
  body { background: var(--backdrop); position: relative; font-family: "Lato", sans-serif; }

  .card {
    position: absolute;
    left: 120px;
    width: 960px;
    height: 548px;
    background: var(--paper);
    border-radius: 36px;
    overflow: hidden;
  }
  .card--services { top: 30px; }
  .card--contact { top: 620px; }

  /* brand lockup */
  .brand { position: absolute; display: flex; align-items: center; gap: 22px; }
  .brand__square { width: 58px; height: 58px; background: var(--orange); flex: none; }
  .brand__rule { width: 2px; height: 96px; background: var(--orange); flex: none; }
  .brand__text { font-family: "Montserrat", sans-serif; line-height: 1.15; }
  .brand__name { font-weight: 700; font-size: 30px; color: var(--orange); letter-spacing: 0.5px; }
  .brand__phone { font-weight: 400; font-size: 20px; color: var(--orange); letter-spacing: 3px; margin-top: 6px; }

  /* services side */
  .services { position: absolute; right: 90px; top: 64px; text-align: right; }
  .services__tagline { font-weight: 900; font-size: 30px; color: var(--orange); margin-bottom: 14px; padding-right: 32px; }
  .services__list { list-style: none; }
  .services__item {
    font-size: 23px; color: var(--ink); line-height: 38px;
    display: flex; justify-content: flex-end; align-items: center; gap: 16px;
  }
  .arrow { width: 0; height: 0; border-top: 7px solid transparent; border-bottom: 7px solid transparent; border-right: 13px solid var(--orange); }

  .band { position: absolute; }
  .card--services .band--orange { left: 0; top: 420px; width: 620px; height: 74px; background: var(--orange); }
  .card--services .band--grey { left: 634px; top: 352px; right: 0; height: 106px; background: var(--grey); }

  /* contact side */
  .person { position: absolute; right: 130px; top: 104px; font-family: "Montserrat", sans-serif; font-size: 42px; color: var(--ink); }
  .person__first { font-weight: 700; }
  .person__last { font-weight: 300; letter-spacing: 1px; }
  .person__mark { position: absolute; right: 70px; top: 96px; }

  .contact { position: absolute; right: 76px; top: 262px; text-align: right; }
  .contact__row { display: flex; justify-content: flex-end; align-items: center; gap: 14px; font-size: 25px; color: var(--ink); line-height: 44px; }
  .contact__icon { width: 24px; height: 24px; fill: var(--ink); }

  .card--contact .band--grey { left: 0; top: 448px; width: 560px; height: 70px; background: var(--grey); clip-path: polygon(0 0, 88% 0, 100% 100%, 0 100%); }
  .card--contact .band--orange { left: 490px; top: 366px; right: 0; height: 110px; background: var(--orange); clip-path: polygon(0 0, 100% 0, 100% 100%, 12% 100%, 0 12%); }
  .abn { position: absolute; right: 150px; top: 392px; font-size: 30px; color: var(--paper); letter-spacing: 1px; }
  .abn__rule { position: absolute; right: 0; top: 412px; width: 130px; height: 1px; background: rgba(255,255,255,0.7); }
</style>
</head>
<body>

<section class="card card--services" aria-label="Card front: services">
  <div class="services">
    <p class="services__tagline">For all your concreting solutions</p>
    <ul class="services__list">
      <li class="services__item">Excavation <span class="arrow"></span></li>
      <li class="services__item">Exposed &amp; colour concrete <span class="arrow"></span></li>
      <li class="services__item">House &amp; shed slabs <span class="arrow"></span></li>
      <li class="services__item">Driveways <span class="arrow"></span></li>
      <li class="services__item">Landing &amp; steps <span class="arrow"></span></li>
    </ul>
  </div>

  <div class="brand" style="left:70px; top:270px;">
    <span class="brand__square"></span>
    <span class="brand__rule"></span>
    <div class="brand__text">
      <p class="brand__name">ASHBY PAVING WORKS</p>
      <p class="brand__phone">0412885107</p>
    </div>
  </div>

  <div class="band band--grey"></div>
  <div class="band band--orange"></div>
</section>

<section class="card card--contact" aria-label="Card back: contact details">
  <div class="brand" style="left:90px; top:200px;">
    <span class="brand__square"></span>
    <span class="brand__rule"></span>
    <div class="brand__text">
      <p class="brand__name">ASHBY PAVING WORKS</p>
      <p class="brand__phone">0412885107</p>
    </div>
  </div>

  <p class="person"><span class="person__first">Mark</span> <span class="person__last">LOWRY</span></p>
  <svg class="person__mark" width="40" height="60" viewBox="0 0 40 60" aria-hidden="true">
    <polygon points="28,0 6,44 38,60" fill="var(--orange)"/>
  </svg>

  <div class="contact">
    <p class="contact__row">0412885107
      <svg class="contact__icon" viewBox="0 0 24 24" aria-hidden="true"><path d="M6.6 10.8a15 15 0 0 0 6.6 6.6l2.2-2.2a1 1 0 0 1 1-.25 11.4 11.4 0 0 0 3.6.57 1 1 0 0 1 1 1V20a1 1 0 0 1-1 1A17 17 0 0 1 3 4a1 1 0 0 1 1-1h3.5a1 1 0 0 1 1 1c0 1.25.2 2.45.57 3.57a1 1 0 0 1-.25 1z"/></svg>
    </p>
    <p class="contact__row">marklowry@pavemail.com.au
      <svg class="contact__icon" viewBox="0 0 24 24" aria-hidden="true"><path d="M2 5h20v14H2z M4 7v.5l8 5.5 8-5.5V7z" fill-rule="evenodd"/></svg>
    </p>
  </div>

  <div class="band band--grey"></div>
  <div class="band band--orange"></div>
  <p class="abn">ABN 27613048852</p>
  <span class="abn__rule"></span>
</section>

</body>
</html>
```